Online retailer needs a Quirky yet professionally designed double sided business car

We mainly sell kitchen and home accessories but pretty much anything new and in demand. Have a look at our site and then come up with designs.
Design to be really catching and want people to visit the website.
Final details such as number, director name and email address will be given to the designer of the winning business card.

Www.zapfinda.com

Ideas out of the norm also welcome!!

```html
<!DOCTYPE html>
<html lang="en">
<head>
<meta charset="utf-8">
<title>Zapfinda – Business Card</title>
<link rel="stylesheet" href="https://fonts.googleapis.com/css2?family=Comfortaa:wght@400;700&family=Open+Sans:wght@400;600&display=swap">
<style>
  :root {
    --orange-deep: #e0561a;
    --orange-mid: #ec7a25;
    --orange-light: #f3b04e;
    --ink: #1d1d1d;
    --white: #ffffff;
    --paper: #f7f7f7;
    --grey-text: #6e6e6e;
    --accent-text: #e06a1c;
    --bg-top: #4b4c4c;
    --bg-bottom: #d2d2d2;
    --dot-one: #2f5f98;
    --dot-two: #2aa3d8;
    --dot-three: #5aa33a;
  }
  * { box-sizing: border-box; margin: 0; padding: 0; }
  html, body { width: 1200px; height: 675px; overflow: hidden; }
  body {
    background: linear-gradient(180deg, var(--bg-top) 0%, var(--bg-bottom) 100%);
    font-family: "Open Sans", sans-serif;
    position: relative;
  }
  .card {
    position: absolute;
    top: 188px;
    width: 525px;
    height: 300px;
    overflow: hidden;
    box-shadow: 0 10px 24px rgba(0,0,0,0.35);
  }
  /* Front */
  .card--front {
    left: 45px;
    background: linear-gradient(160deg, var(--orange-light) 0%, var(--orange-mid) 45%, var(--orange-deep) 100%);
  }
  .front__brand {
    position: absolute;
    left: 48px;
    top: 38px;
    font-family: "Comfortaa", sans-serif;
    font-weight: 700;
    font-size: 66px;
    color: var(--ink);
    letter-spacing: 1px;
  }
  .front__rule {
    position: absolute;
    left: 150px; top: 120px;
    width: 330px; height: 1px;
    background: rgba(120,60,10,0.35);
  }
  .front__tagline {
    position: absolute;
    left: 175px; top: 126px;
    font-family: "Comfortaa", sans-serif;
    font-size: 20px;
    color: var(--white);
  }
  .front__url {
    position: absolute;
    left: 48px; top: 160px;
    font-family: "Comfortaa", sans-serif;
    font-weight: 700;
    font-size: 30px;
    letter-spacing: 4px;
    color: var(--ink);
  }
  .front__band {
    position: absolute;
    left: 0; top: 226px;
    width: 100%; height: 12px;
    background: var(--ink);
    border-bottom: 3px solid var(--white);
  }
  .front__links {
    position: absolute;
    left: 210px; top: 208px;
    display: flex;
    gap: 56px;
  }
  .front__link {
    width: 46px; height: 46px;
    border-radius: 50%;
    border: 3px solid var(--white);
  }
  .front__link--one { background: var(--dot-one); }
  .front__link--two { background: var(--dot-two); }
  .front__link--three { background: var(--dot-three); }

  /* Back */
  .card--back {
    left: 630px;
    background: var(--paper);
  }
  .back__header { position: absolute; inset: 0; }
  .back__name {
    position: absolute;
    left: 40px; top: 30px;
    font-family: "Comfortaa", sans-serif;
    font-weight: 700;
    font-size: 32px;
    color: var(--white);
  }
  .back__role {
    position: absolute;
    left: 64px; top: 72px;
    font-family: "Comfortaa", sans-serif;
    font-size: 22px;
    color: var(--grey-text);
  }
  .back__contacts {
    position: absolute;
    left: 40px; top: 168px;
    list-style: none;
    font-size: 13px;
    line-height: 19px;
    color: var(--accent-text);
  }
  .back__brand {
    position: absolute;
    right: 36px; top: 210px;
    text-align: right;
  }
  .back__brand-name {
    font-family: "Comfortaa", sans-serif;
    font-weight: 700;
    font-size: 38px;
    color: var(--ink);
  }
  .back__brand-tagline {
    margin-top: 2px;
    padding-top: 2px;
    border-top: 1px solid #999;
    font-family: "Comfortaa", sans-serif;
    font-size: 12px;
    color: var(--accent-text);
  }
</style>
</head>
<body>
  <section class="card card--front" aria-label="Card front">
    <div class="front__brand">Zapfinda</div>
    <div class="front__rule"></div>
    <div class="front__tagline">finds for every home</div>
    <div class="front__url">www.zapfinda.com</div>
    <div class="front__band"></div>
    <div class="front__links">
      <span class="front__link front__link--one"></span>
      <span class="front__link front__link--two"></span>
      <span class="front__link front__link--three"></span>
    </div>
  </section>

  <section class="card card--back" aria-label="Card back">
    <svg class="back__header" width="525" height="300" viewBox="0 0 525 300" aria-hidden="true">
      <defs>
        <linearGradient id="headerFill" x1="0" y1="0" x2="1" y2="0">
          <stop offset="0" stop-color="#ea7a26"/>
          <stop offset="1" stop-color="#f2aa46"/>
        </linearGradient>
      </defs>
      <polygon points="0,0 525,0 525,190 0,120" fill="url(#headerFill)"/>
    </svg>
    <div class="back__name">John Doe</div>
    <div class="back__role">position</div>
    <ul class="back__contacts">
      <li>address: johndoe Street, johndoe, johndoe</li>
      <li>e-mail: john.doe@e-mail.com</li>
      <li>skype: John Doe</li>
      <li>tel. 123 456 7890</li>
      <li>web. www.zapfinda.com</li>
    </ul>
    <div class="back__brand">
      <div class="back__brand-name">Zapfinda</div>
      <div class="back__brand-tagline">finds for every home</div>
    </div>
  </section>
</body>
</html>
```